Personal Development Model Graphic

I am creating a Personal Development/Coaching business and website and need some assistance with the development of a graphic that represents my methodology. I have already done what I consider to be a working version, but now it's time to have a professional design eye take a look at it and improve.

Specifically, I need assistance on color usage. I'd like each of the 8 areas of the model to have a color, and I've tried to utilize colors I feel are representative of the specific area(for example, purple for spirituality) but it doesn't really work for everything and perhaps additional thought could be put to that aspect of it.

Also, the model needs to work in reverse of the way it's pictured in the attached JPEG. So Friends needs to be first (top center)and then going clockwise, Spirituality needs to be in the 1:00 position not the 11:00 position and then continue around to Community, Family, Exercise, Career, Art/Creativity, and last at 11:00 Sexuality. I was going to update it before uploading, but I'm having trouble with Photoshop and just decided to pull the trigger on having a designer do it.

Thank you in advance for your creativity and ideas!

Industry/Entity Type

Business

Requirements
Nice to have
• It would be fantastic if it could feel modern, and high tech. I realize this is difficult with circles! But whatever you can do.

On color usage, it would again be wonderful to have colors that are more modern than traditional. I'll leave that to your discretion.

```html
<!DOCTYPE html>
<html lang="en">
<head>
<meta charset="UTF-8">
<title>Happiness Model</title>
<link rel="stylesheet" href="https://fonts.googleapis.com/css2?family=Signika:wght@300;400&display=swap">
<style>
  :root {
    --bg-center: #ffffff;
    --bg-edge: #e6e7e9;
    --shadow: #8a8a8a;
    --text: #ffffff;
    --core: #4f3f6b;
    --friends: #e9078b;
    --spirituality: #fcd800;
    --community: #f68b1f;
    --family: #ed1c2e;
    --exercise: #8cc63f;
    --career: #7a3e97;
    --art: #0094ad;
    --sexuality: #00adee;
  }
  html, body {
    margin: 0;
    padding: 0;
    width: 1200px;
    height: 1000px;
    overflow: hidden;
  }
  .model {
    display: block;
    width: 1200px;
    height: 1000px;
  }
  .stage-bg { fill: url(#stageGlow); }
  .node-shadow { fill: var(--shadow); opacity: .45; filter: url(#softBlur); }
  .node-body { stroke: none; }
  .gloss-top { fill: #ffffff; opacity: .16; }
  .gloss-low { fill: #ffffff; opacity: .09; }
  .gloss-rim { fill: none; stroke: #ffffff; stroke-opacity: .22; stroke-width: 1.5; }
  .node-label {
    font-family: "Signika", "Trebuchet MS", sans-serif;
    font-weight: 300;
    fill: var(--text);
    text-anchor: middle;
    dominant-baseline: central;
    font-size: 24px;
  }
  .node-label--core { font-size: 37px; }
  .node-label--small { font-size: 21px; }
  .node-label--tiny { font-size: 19px; }
  .node--core .node-body { fill: var(--core); }
  .node--friends .node-body { fill: var(--friends); }
  .node--spirituality .node-body { fill: var(--spirituality); }
  .node--community .node-body { fill: var(--community); }
  .node--family .node-body { fill: var(--family); }
  .node--exercise .node-body { fill: var(--exercise); }
  .node--career .node-body { fill: var(--career); }
  .node--art .node-body { fill: var(--art); }
  .node--sexuality .node-body { fill: var(--sexuality); }
</style>
</head>
<body>
<svg class="model" viewBox="0 0 1200 1000" xmlns="http://www.w3.org/2000/svg" role="img" aria-label="Happiness at the centre surrounded by Friends, Spirituality, Community, Family, Exercise, Career, Art/Creativity and Sexuality">
  <defs>
    <radialGradient id="stageGlow" cx="50%" cy="50%" r="62%">
      <stop offset="0" stop-color="var(--bg-center)"/>
      <stop offset=".7" stop-color="var(--bg-center)"/>
      <stop offset="1" stop-color="var(--bg-edge)"/>
    </radialGradient>
    <filter id="softBlur" x="-50%" y="-200%" width="200%" height="500%">
      <feGaussianBlur stdDeviation="4"/>
    </filter>
  </defs>

  <rect class="stage-bg" width="1200" height="1000"/>

  <!-- Centre -->
  <g class="node node--core" transform="translate(600 493)">
    <ellipse class="node-shadow" cx="0" cy="134" rx="95" ry="7"/>
    <circle class="node-body" r="135"/>
    <circle class="gloss-top" cx="-2" cy="-70" r="74"/>
    <circle class="gloss-low" cx="40" cy="60" r="110"/>
    <text class="node-label node-label--core" x="0" y="3">Happiness</text>
  </g>

  <g class="node node--friends" transform="translate(599 257)">
    <ellipse class="node-shadow" cx="0" cy="72" rx="48" ry="5"/>
    <circle class="node-body" r="71"/>
    <circle class="gloss-top" cx="0" cy="-12" r="56"/>
    <circle class="gloss-low" cx="-10" cy="22" r="52"/>
    <text class="node-label" x="0" y="1">Friends</text>
  </g>

  <g class="node node--spirituality" transform="translate(766 328)">
    <ellipse class="node-shadow" cx="0" cy="72" rx="48" ry="5"/>
    <circle class="node-body" r="71"/>
    <circle class="gloss-top" cx="4" cy="-12" r="56"/>
    <circle class="gloss-low" cx="-8" cy="20" r="50"/>
    <text class="node-label" x="0" y="1">Spirituality</text>
  </g>

  <g class="node node--community" transform="translate(835 494)">
    <ellipse class="node-shadow" cx="0" cy="72" rx="48" ry="5"/>
    <circle class="node-body" r="71"/>
    <circle class="gloss-top" cx="0" cy="-8" r="52"/>
    <circle class="gloss-low" cx="10" cy="10" r="58"/>
    <text class="node-label node-label--small" x="0" y="1">Community</text>
  </g>

  <g class="node node--family" transform="translate(766 660)">
    <ellipse class="node-shadow" cx="0" cy="72" rx="48" ry="5"/>
    <circle class="node-body" r="71"/>
    <circle class="gloss-top" cx="-4" cy="-14" r="54"/>
    <circle class="gloss-low" cx="8" cy="14" r="56"/>
    <text class="node-label" x="0" y="2">Family</text>
  </g>

  <g class="node node--exercise" transform="translate(599 729)">
    <ellipse class="node-shadow" cx="0" cy="72" rx="48" ry="5"/>
    <circle class="node-body" r="71"/>
    <circle class="gloss-top" cx="-2" cy="-14" r="52"/>
    <circle class="gloss-low" cx="0" cy="16" r="54"/>
    <text class="node-label" x="0" y="6">Exercise</text>
  </g>

  <g class="node node--career" transform="translate(433 660)">
    <ellipse class="node-shadow" cx="0" cy="72" rx="48" ry="5"/>
    <circle class="node-body" r="71"/>
    <circle class="gloss-top" cx="4" cy="-14" r="52"/>
    <circle class="gloss-low" cx="-6" cy="14" r="56"/>
    <text class="node-label" x="-4" y="2">Career</text>
  </g>

  <g class="node node--art" transform="translate(365 494)">
    <ellipse class="node-shadow" cx="0" cy="72" rx="48" ry="5"/>
    <circle class="node-body" r="71"/>
    <circle class="gloss-top" cx="-6" cy="-6" r="50"/>
    <circle class="gloss-low" cx="12" cy="8" r="56"/>
    <text class="node-label node-label--tiny" x="0" y="2">Art/Creativity</text>
  </g>

  <g class="node node--sexuality" transform="translate(433 328)">
    <ellipse class="node-shadow" cx="0" cy="72" rx="48" ry="5"/>
    <circle class="node-body" r="71"/>
    <circle class="gloss-top" cx="4" cy="-14" r="54"/>
    <circle class="gloss-low" cx="16" cy="14" r="56"/>
    <text class="node-label" x="2" y="2">Sexuality</text>
  </g>
</svg>
</body>
</html>
```